Web Design Project

Psychotherapy and Counselling Practice needs a landing page web design.

My business "Harbourlight Consulting" specialises in the treatment of Anxiety and Depression with a holistic approach, endeavouring to unlock the key that holds us to ransom in a life that is imbalanced, frustrating, and ultimately of our own making due to our own perceptions and behaviours.

There is much that impacts us which we cannot change, but we are always in control of how we think, and how we frame our experiences.....learning to challenge those thoughts and behaviours that are destructive and disempowering opens up a world of joyful possibility. Life is about making choices, learn to make wiser and healthier choices.......

Harbourlight Consulting has a client base of individual clients but will seek to expand to offer services to the Corporate world by offering an adjunct to employers for established "Wellness Programs".

Harbourlight Consulting is a highly professional, ethically bound business, with the needs of the client at the forefront of all we do.

Harbourlight Consulting wishes to avoid the usual "jargon driven" psychobabble offered on many counselling web pages. It aims to be stylishly presented, clean in look and with as few "words" as possible and a largely white background (faster loading and more powerful impact of what is stated), those words contained in the webpage should be meaningful, persuasive and have an impact simply at glance. Harbourlight does not want , or expect, those prospective clients in need of support , to be reading through volumes of industry driven cliches.

At this point Harbourlight is just looking for a high quality landing page. However in time this will likely expand to include other sections such as case studies, video content etc.

Target Market(s)

Those in need of emotional support, suffering mental health issues, and those simply wanting to become self aware supported by a mindful therapist.

Industry/Entity Type

Industry

Requirements
Must have
• The design must incorporate the Harbourlight logo and colour schemes found on the attached files.

```html
<!DOCTYPE html>
<html lang="en">
<head>
<meta charset="utf-8">
<title>Harbourlight — Home</title>
<link rel="stylesheet" href="https://fonts.googleapis.com/css2?family=Lato:wght@300;400;700&display=swap">
<style>
  :root {
    --green: #85ab12;
    --green-dark: #5f8a0a;
    --green-light: #b6dc4a;
    --leaf: #7cc428;
    --grey-text: #666666;
    --bubble: #666666;
    --bubble-dark: #4f4f4f;
    --panel: #e2e2e2;
    --white: #ffffff;
  }
  * { box-sizing: border-box; margin: 0; padding: 0; }
  html, body { width: 1200px; height: 759px; overflow: hidden; }
  body {
    position: relative;
    font-family: "Lato", sans-serif;
    background: radial-gradient(ellipse 560px 420px at 600px 420px, #ffffff 0%, #efefef 55%, #d6d6d6 100%);
  }

  .site-header { position: absolute; left: 0; top: 0; width: 1200px; height: 189px; }
  .brand {
    position: absolute; left: 0; top: 86px; width: 1200px;
    text-align: center;
    font-weight: 300; font-size: 30px; letter-spacing: 0.5px;
    color: var(--green);
  }

  .main-nav {
    position: absolute; left: 0; top: 189px; width: 1200px; height: 46px;
    background: var(--green);
  }
  .main-nav .nav-panel {
    position: absolute; left: 179px; top: 0; width: 843px; height: 46px;
    background: var(--panel);
    border-top: 1px solid #c9d98f; border-bottom: 1px solid #cfcfcf;
    display: flex; justify-content: center; align-items: center; gap: 14px;
    padding-left: 4px;
  }
  .nav-link {
    font-weight: 300; font-size: 20px; letter-spacing: -1.4px;
    color: var(--grey-text); text-decoration: none; text-transform: uppercase;
    display: flex; align-items: center;
  }
  .nav-link.is-active { color: var(--green); }
  .nav-link .leaf-mark {
    width: 9px; height: 13px; margin-right: 3px; margin-top: -6px;
    background: var(--green); border-radius: 0 100% 0 100%;
    transform: rotate(-10deg);
  }

  .feature {
    position: absolute; top: 295px; width: 270px; height: 240px;
  }
  .feature .ground-shadow {
    position: absolute; left: -10px; top: 205px; width: 260px; height: 32px;
    border-radius: 50%;
    background: radial-gradient(ellipse at center, rgba(0,0,0,0.25) 0%, rgba(0,0,0,0) 70%);
  }
  .feature .leaf-area {
    position: absolute; left: 30px; top: 55px; width: 236px; height: 160px;
    border-radius: 40px;
    background: radial-gradient(ellipse at 60% 60%, rgba(124,196,40,0.85) 0%, rgba(124,196,40,0.45) 50%, rgba(124,196,40,0) 75%);
  }
  .feature .bubble {
    position: absolute; left: 0; top: 0; width: 206px; height: 206px;
    border-radius: 50%;
    background: radial-gradient(circle at 50% 40%, #6e6e6e 0%, var(--bubble) 60%, var(--bubble-dark) 100%);
    box-shadow: inset 0 0 0 2px rgba(255,255,255,0.12), 0 2px 4px rgba(0,0,0,0.25);
    color: var(--white); text-align: center;
    text-shadow: 0 1px 2px rgba(0,0,0,0.5);
  }
  .bubble h2 {
    position: absolute; left: 0; top: 31px; width: 100%;
    font-weight: 700; font-size: 22px; letter-spacing: -1.2px;
    text-transform: uppercase;
  }
  .bubble p {
    position: absolute; left: 20px; top: 71px; width: 166px;
    font-size: 13px; line-height: 15.5px; letter-spacing: -0.3px;
  }
  .bubble .quote-text { left: 14px; width: 178px; }
  .bubble .quote-author {
    top: 133px; font-weight: 700; font-size: 13px; text-transform: uppercase;
  }
  .read-more {
    position: absolute; left: 64px; top: 164px; width: 75px; height: 21px;
    border: 1px solid rgba(255,255,255,0.75); border-radius: 11px;
    font-weight: 700; font-size: 12px; letter-spacing: -0.8px; line-height: 19px;
    color: var(--white); text-decoration: none; text-transform: uppercase;
  }
  .feature-about { left: 227px; }
  .feature-quote { left: 490px; }
  .feature-services { left: 748px; }

  .social {
    position: absolute; left: 508px; top: 576px; width: 190px; height: 120px;
  }
  .social-dot {
    position: absolute; top: 2px; width: 57px; height: 57px; border-radius: 50%;
    background: radial-gradient(circle at 50% 30%, var(--green-light) 0%, #8fc11c 55%, var(--green-dark) 100%);
    border: 2px solid #7ea818;
  }
  .social-dot.is-reflection {
    top: 62px; opacity: 0.22;
    -webkit-mask-image: linear-gradient(to bottom, #000, transparent);
    mask-image: linear-gradient(to bottom, #000, transparent);
  }
  .social-dot:nth-of-type(1), .social-dot:nth-of-type(4) { left: 5px; }
  .social-dot:nth-of-type(2), .social-dot:nth-of-type(5) { left: 66px; }
  .social-dot:nth-of-type(3), .social-dot:nth-of-type(6) { left: 127px; }

  .site-footer {
    position: absolute; left: 0; top: 713px; width: 1200px; height: 46px;
    background: var(--green);
    color: var(--white); text-align: center;
    font-size: 14px; letter-spacing: -0.8px; line-height: 46px;
  }
</style>
</head>
<body>
  <header class="site-header">
    <div class="brand">HARBOURLIGHT</div>
  </header>

  <nav class="main-nav">
    <div class="nav-panel">
      <a class="nav-link is-active" href="#"><span class="leaf-mark"></span>Home</a>
      <a class="nav-link" href="#">About Us</a>
      <a class="nav-link" href="#">Services</a>
      <a class="nav-link" href="#">Case Studies</a>
      <a class="nav-link" href="#">Contact Us</a>
    </div>
  </nav>

  <section class="feature feature-about">
    <div class="ground-shadow"></div>
    <div class="leaf-area" role="img" aria-label="Green leaf with dew drops cradling the panel"></div>
    <div class="bubble">
      <h2>About Us</h2>
      <p>Harbourlight Consulting is a highly professional, ethically bound business, with the needs of the client at the forefront of all we do.</p>
      <a class="read-more" href="#">Read More</a>
    </div>
  </section>

  <section class="feature feature-quote">
    <div class="ground-shadow"></div>
    <div class="leaf-area" role="img" aria-label="Green leaf with dew drops cradling the panel"></div>
    <div class="bubble">
      <p class="quote-text">“Just living is not enough, one must have sunshine, freedom, and a little flower”</p>
      <p class="quote-author">Elias<br>Marrow</p>
    </div>
  </section>

  <section class="feature feature-services">
    <div class="ground-shadow"></div>
    <div class="leaf-area" role="img" aria-label="Green leaf with dew drops cradling the panel"></div>
    <div class="bubble">
      <h2>Services</h2>
      <p>Psychotherapy &amp; Counselling Practice, Wellness Programs, Individual clients, Corporate services</p>
      <a class="read-more" href="#">Read More</a>
    </div>
  </section>

  <div class="social" aria-label="Social links">
    <a class="social-dot" href="#" aria-label="Professional network"></a>
    <a class="social-dot" href="#" aria-label="Social page"></a>
    <a class="social-dot" href="#" aria-label="News feed"></a>
    <span class="social-dot is-reflection"></span>
    <span class="social-dot is-reflection"></span>
    <span class="social-dot is-reflection"></span>
  </div>

  <footer class="site-footer">© 2013 HARBOURLIGHT.</footer>
</body>
</html>
```